High end Desks & Chairs Distibutor looking for a brochure desin

Harbor Loom G.P, Canadian Furniture and Stationery Distributor, (very attractive patented design -mainly Desks & Chairs-), Adjstable to fit many needs.
3 folds flyer,
Bilangual text and photos provided,
Use same colors as Logo
Flyer Disign shoul reflect Ergonomy, High End User Freindly Products, Eco Freindly materials,

Target Market(s)

Limited mobility people
Children from 4 to 17 years old
Multi porpuses desks users

Industry/Entity Type

Distributor

Requirements
Nice to have
• Have a hint for Ergonomic, Adjustable, multi-purpose use.

```html
<!DOCTYPE html>
<html lang="en">
<head>
<meta charset="utf-8">
<title>Harbor Loom G.P — Tri-fold Brochure</title>
<link rel="stylesheet" href="https://fonts.googleapis.com/css2?family=Roboto+Condensed:wght@400;700&family=Open+Sans:wght@400;600&family=Montserrat:wght@700&display=swap">
<style>
  :root {
    --navy: #2a3945;
    --navy-deep: #22303a;
    --gold: #e0b455;
    --white: #ffffff;
    --ink: #2a3945;
    --page: #ffffff;
    --wood: #e6c68a;
    --wood-light: #f3e4c4;
    --steel: #dde1e6;
    --steel-light: #f3f5f7;
  }
  * { box-sizing: border-box; margin: 0; padding: 0; }
  html, body { width: 1200px; height: 907px; overflow: hidden; background: var(--page); }
  .canvas { position: relative; width: 1200px; height: 907px; }
  .brochure { position: absolute; left: 82px; top: 66px; width: 1048px; height: 746px; }
  .panel { position: absolute; top: 0; height: 746px; overflow: hidden; }
  .panel--about { left: 0; width: 355px; background: var(--white); }
  .panel--feature { left: 355px; width: 348px; background: var(--navy); }
  .panel--cover { left: 703px; width: 345px; background: var(--white); }
  .panel svg.bands { position: absolute; left: 0; top: 0; }

  .placeholder { position: absolute; }
  .about-backdrop { left: 0; top: 0; width: 355px; height: 640px;
    background: linear-gradient(180deg, #ffffff 0%, #fafafa 55%, #f1f1f1 100%); }
  .about-desk { left: 64px; top: 370px; width: 280px; height: 360px; border-radius: 8px;
    background: linear-gradient(170deg, var(--wood) 0%, var(--wood-light) 38%, var(--steel-light) 62%, var(--steel) 100%);
    box-shadow: 0 4px 14px rgba(42,57,69,.18); }
  .feature-room { left: 0; top: 0; width: 348px; height: 530px;
    background: linear-gradient(180deg, #2f3e49 0%, #3a4a56 55%, #2c3b46 100%); opacity: .9; }
  .cover-desk { left: 16px; top: 140px; width: 313px; height: 250px; border-radius: 8px;
    background: linear-gradient(165deg, var(--steel-light) 0%, #e9ecef 50%, var(--steel) 100%);
    box-shadow: 0 4px 14px rgba(42,57,69,.15); }

  .feature-badge { position: absolute; display: flex; flex-direction: column; align-items: center; width: 170px; text-align: center; }
  .feature-badge .icon { width: 58px; height: 58px; }
  .feature-badge h3 { font: 700 17px/1 "Roboto Condensed", sans-serif; color: var(--ink); margin-top: 12px; }
  .feature-badge p { font: 400 10.5px/1.2 "Open Sans", sans-serif; color: var(--ink); margin-top: 3px; }
  .badge-high-end { left: 8px; top: 54px; }
  .badge-eco { left: 183px; top: 56px; }

  .about-title { position: absolute; left: 26px; top: 184px; font: 700 25px/1 "Roboto Condensed", sans-serif; color: var(--ink); }
  .about-list { position: absolute; left: 30px; top: 233px; width: 270px; list-style: none; }
  .about-list li { position: relative; padding-left: 16px; font: 400 11.5px/1.3 "Open Sans", sans-serif; color: var(--ink); margin-bottom: 13px; }
  .about-list li::before { content: ""; position: absolute; left: 0; top: 5px; width: 6px; height: 6px; border-radius: 50%; background: var(--gold); }

  .brand { position: absolute; display: flex; align-items: center; gap: 8px; font: 700 20px/1 "Roboto Condensed", sans-serif; white-space: nowrap; }
  .brand .mark { width: 12px; height: 12px; border-radius: 50%; }
  .brand--light { left: 0; width: 348px; top: 141px; justify-content: center; color: var(--white); }
  .brand--light .mark { background: var(--white); }
  .brand--dark { left: 0; width: 345px; top: 50px; justify-content: center; color: var(--ink); font-size: 26px; }
  .brand--dark .mark { background: var(--ink); width: 14px; height: 14px; }

  .seal { position: absolute; left: 42px; top: 334px; width: 264px; height: 264px; border-radius: 50%; background: var(--white); border: 6px solid var(--navy);
    display: flex; flex-direction: column; align-items: center; justify-content: center; text-align: center; }
  .seal .l1 { font: 700 28px/1 "Roboto Condensed", sans-serif; color: var(--ink); }
  .seal .l2 { font: 400 27px/1.15 "Open Sans", sans-serif; color: var(--ink); letter-spacing: -.5px; }
  .seal .l3 { font: 700 24px/1 "Montserrat", sans-serif; color: var(--gold); margin-top: 2px; }
  .seal .l4 { font: 700 28px/1.1 "Roboto Condensed", sans-serif; color: var(--ink); margin-top: 4px; }

  .phone { position: absolute; left: 0; width: 348px; top: 636px; text-align: center; font: 700 41px/1 "Roboto Condensed", sans-serif; color: var(--ink); letter-spacing: .5px; }
  .web { position: absolute; left: 0; top: 689px; text-align: center; font: 400 15px/1 "Open Sans", sans-serif; color: var(--ink); letter-spacing: 4.5px; }
  .panel--feature .web { width: 348px; }
  .panel--cover .web { width: 345px; }

  .cover-title { position: absolute; left: 0; width: 345px; top: 488px; text-align: center; }
  .cover-title .t1 { display: block; font: 700 66px/1 "Roboto Condensed", sans-serif; color: var(--ink); transform: scaleY(1.25); transform-origin: top center; }
  .cover-title .t2 { display: block; font: 700 62px/1 "Roboto Condensed", sans-serif; color: var(--white); margin-top: 20px; }
  .cover-title .t3 { display: block; font: 400 28px/1 "Roboto Condensed", sans-serif; color: var(--white); margin-top: 6px; }
</style>
</head>
<body>
<div class="canvas">
  <div class="brochure">

    <section class="panel panel--about">
      <div class="placeholder about-backdrop" role="img" aria-label="Soft photo of a bright room behind the desk"></div>
      <svg class="bands" width="355" height="746" aria-hidden="true">
        <polygon points="0,622 355,505 355,520 0,638" fill="var(--navy)"/>
        <polygon points="0,646 355,529 355,746 0,746" fill="var(--gold)"/>
      </svg>
      <div class="placeholder about-desk" role="img" aria-label="Photo of a height-adjustable tilting desk with wooden top and white pedestal base"></div>

      <div class="feature-badge badge-high-end">
        <svg class="icon" viewBox="0 0 58 58" aria-hidden="true">
          <circle cx="29" cy="29" r="28" fill="var(--navy)"/>
          <circle cx="29" cy="29" r="25" fill="var(--gold)"/>
          <path d="M15 20h5l4 14h14l3-10H22" fill="none" stroke="var(--navy)" stroke-width="2.2" stroke-linejoin="round"/>
          <circle cx="26" cy="39" r="2" fill="var(--navy)"/><circle cx="36" cy="39" r="2" fill="var(--navy)"/>
        </svg>
        <h3>HIGH END</h3>
        <p>USER FREINDLY PRODUCTS</p>
      </div>
      <div class="feature-badge badge-eco">
        <svg class="icon" viewBox="0 0 58 58" aria-hidden="true">
          <circle cx="29" cy="29" r="28" fill="var(--navy)"/>
          <circle cx="29" cy="29" r="25" fill="var(--gold)"/>
          <path d="M29 16c6 4 6 10 0 13c-6-3-6-9 0-13z" fill="var(--navy)"/>
          <path d="M17 36c3-7 9-8 12-4c-3 5-9 7-12 4z" fill="var(--navy)"/>
          <path d="M41 36c-3-7-9-8-12-4c3 5 9 7 12 4z" fill="var(--navy)"/>
        </svg>
        <h3>ECO FREINDLY</h3>
        <p>MATERIALS</p>
      </div>

      <h2 class="about-title">WE ARE</h2>
      <ul class="about-list">
        <li>Harbor Loom G.P,</li>
        <li>Canadian Furniture and Stationery Distributor (very attractive patented design -mainly Desks &amp; Chairs-)</li>
        <li>Adjstable to fit many needs.</li>
      </ul>
    </section>

    <section class="panel panel--feature">
      <div class="placeholder feature-room" role="img" aria-label="Dim photo of a furnished living room"></div>
      <svg class="bands" width="348" height="746" aria-hidden="true">
        <polygon points="0,520 348,398 348,414 0,536" fill="var(--white)"/>
        <polygon points="0,536 348,414 348,746 0,746" fill="var(--gold)"/>
      </svg>
      <div class="brand brand--light"><span class="mark"></span>Harbor Loom G.P</div>
      <div class="seal">
        <span class="l1">VERY ATTRACTIVE</span>
        <span class="l2">patented design</span>
        <span class="l3">MAINLY</span>
        <span class="l4">DESKS &amp; CHAIRS</span>
      </div>
      <div class="phone">0123456789</div>
      <div class="web">www.harborloomgp.ca</div>
    </section>

    <section class="panel panel--cover">
      <svg class="bands" width="345" height="746" aria-hidden="true">
        <rect x="0" y="400" width="345" height="346" fill="var(--gold)"/>
        <rect x="0" y="404" width="345" height="8" fill="var(--navy)"/>
      </svg>
      <div class="brand brand--dark"><span class="mark"></span>Harbor Loom G.P</div>
      <div class="placeholder cover-desk" role="img" aria-label="Photo of a white adjustable children's study desk with tilting top"></div>
      <h1 class="cover-title">
        <span class="t1">CANADIAN</span>
        <span class="t2">FURNITURE</span>
        <span class="t3">and Stationery Distributor</span>
      </h1>
      <div class="web">www.harborloomgp.ca</div>
    </section>

  </div>
</div>
</body>
</html>
```